Etikettendesign für Ergänzungsfuttermittel für Hunde
Zielgruppe
Ich bin Tierphysiotherapeutin und möchte ein Ergänzungsfuttermittel für Hunde erstellen und verkaufen. Dazu benötige ich ein passendes Etikett.
Aufgabenstellung
Das Ergänzungsfuttermittel ist ein Nährstoffpulver zur Unterstützung des Bewegungsapparats. Das soll bitte auch drauf stehen. Des weiteren sind 100% natürliche Inhaltsstoffe drin (Brennessel, Kurkuma, Leinsamen, Hagebutte, Löwenzahn). Es sollte erkennlich sein dass es für Hunde ist. Mein Firmenname ist Anka's Pfotenwerk. Dieser sollte ebenfalls auf dem Etikett stehen. Ich bin mir noch unschlüssig, ob mein Logo mit rauf passt oder nicht. Eine Wiedererkennung sollte gegeben sein. Soll aber nicht zu sehr auffallen. Das Wort 'Bewegungsapparat' sollte jedoch rausstechen. Die Farben sollten nicht zu knallig sein. Ruhige Töne und auf einander abgestimmt. Ich lasse mich überraschen und bedanke mich im Voraus! ♡ Die Maße der Verpackung sind anbei. Es wäre toll, wenn das Etikett einmal komplett rumgeht.
Auf der Rückseite:
Ergänzungsfuttermittel für Hunde
• trägt einer gesunden Gelenkfunktion bei
• zur Unterstützung des gesamten Bewegungsapparats
• für mehr Vitalität und Wohlbefinden
Zusammensetzung: Brennessel, Kurkuma, Hagebutten, Leinsamen, Löwenzahn
Analytische Bestandteile: Rohfaser 2,55%, Feuchtgehalt 12%
Fütterungsempfehlung:
Hunde bis 20kg - 1gr täglich (reicht für 6 Monate)
Hunde ab 20kg - 2gr täglich (reicht für 3 Monate)
Das Pulver kann unter dem Futter gemischt werden.
Nettomasse: 200g
Hinweis: kühl, trocken und lichtgeschützt lagern.

```html
<!DOCTYPE html>
<html lang="de">
<head>
<meta charset="utf-8">
<title>Etikett Nährstoffpulver – Anka's Pfotenwerk</title>
<link href="https://fonts.googleapis.com/css2?family=Quicksand:wght@400;500;600;700&family=Dancing+Script:wght@700&display=swap" rel="stylesheet">
<style>
  :root {
    --page: #f3f1ec;
    --taupe: #a39680;
    --taupe-dark: #7a6d5b;
    --cream: #efebe0;
    --white: #ffffff;
    --ink: #2b2824;
    --ink-soft: #4a453e;
    --accent: #8a5a7a;
  }
  * { margin: 0; padding: 0; box-sizing: border-box; }
  html, body { width: 1200px; height: 846px; overflow: hidden; background: var(--page); }
  body { font-family: "Quicksand", sans-serif; color: var(--ink); position: relative; }

  .label {
    position: absolute; left: 31px; top: 263px;
    width: 1138px; height: 320px;
    background: var(--taupe);
    overflow: hidden;
  }
  .label__band { position: absolute; left: 0; top: 0; width: 100%; height: 52px; background: var(--cream); }

  .info-box {
    position: absolute; background: var(--white);
    padding: 10px 10px;
    font-size: 11.5px; line-height: 1.25; color: var(--ink-soft);
  }
  .info-box h3 { font-size: 13px; font-weight: 700; color: var(--ink); margin-bottom: 3px; }
  .info-box ul { list-style: none; }
  .info-box li::before { content: "• "; }
  .info-box p + p { margin-top: 13px; }

  .info-box--purpose { left: 12px; top: 19px; width: 245px; height: 96px; }
  .info-box--purpose h3 { margin-bottom: 14px; }
  .info-box--purpose li { padding-left: 8px; text-indent: -8px; }
  .info-box--composition { left: 12px; top: 126px; width: 245px; height: 102px; padding-top: 8px; }
  .info-box--maker { left: 12px; top: 237px; width: 245px; height: 60px; padding-top: 6px; }

  .info-box--feeding {
    left: 928px; top: 26px; width: 196px; height: 151px;
    text-align: right; padding: 6px 10px;
  }
  .info-box--feeding h3 { font-size: 11.5px; margin-bottom: 14px; }
  .info-box--feeding .dose { color: var(--ink); }
  .info-box--feeding .dose + .dose { margin-top: 14px; }
  .info-box--feeding .note { margin-top: 14px; }

  .net-weight { position: absolute; right: 18px; top: 183px; color: var(--white); font-weight: 700; font-size: 13.5px; }
  .storage-hint { position: absolute; right: 18px; top: 218px; color: var(--cream); font-size: 11px; text-align: right; line-height: 1.2; }
  .best-before {
    position: absolute; left: 885px; top: 253px; width: 238px; height: 46px;
    background: var(--white); padding: 8px 8px; font-weight: 700; font-size: 12px;
  }

  .brand-card {
    position: absolute; left: 536px; top: 1px; width: 104px; height: 59px;
    background: var(--white); border-radius: 8px;
    display: flex; flex-direction: column; align-items: center; justify-content: center; gap: 4px;
  }
  .brand-card__dot { width: 12px; height: 12px; border-radius: 50%; background: var(--accent); }
  .brand-card__name { font-size: 9.5px; font-weight: 600; color: var(--accent); }

  .front { position: absolute; left: 388px; width: 400px; text-align: center; color: var(--white); }
  .front__title { top: 62px; font-size: 26px; line-height: 32px; font-weight: 500; letter-spacing: 0.5px; }
  .front__subtitle { top: 94px; font-size: 14.5px; line-height: 18px; color: var(--cream); }
  .front__support { top: 134px; font-size: 14px; line-height: 18px; color: var(--cream); }

  .highlight {
    position: absolute; left: 437px; top: 158px; width: 296px; height: 36px;
    background: var(--taupe-dark); border-radius: 18px 8px 18px 8px;
  }
  .highlight__word {
    position: absolute; left: 405px; top: 154px; width: 360px; height: 42px; text-align: center;
    font-family: "Dancing Script", cursive; font-size: 36px; line-height: 42px; color: var(--white);
  }

  .dog-art { position: absolute; left: 448px; top: 206px; width: 200px; height: 96px; }
  .badge { position: absolute; left: 665px; top: 212px; width: 86px; height: 86px; }
  .badge__text {
    position: absolute; inset: 0; display: flex; align-items: center; justify-content: center;
    text-align: center; font-size: 10.5px; line-height: 1.15; color: var(--cream);
    transform: rotate(22deg);
  }
</style>
</head>
<body>
  <main class="label">
    <div class="label__band"></div>

    <section class="info-box info-box--purpose">
      <h3>Ergänzungsfuttermittel für Hunde</h3>
      <ul>
        <li>trägt einer gesunden Gelenkfunktion bei</li>
        <li>zur Unterstützung des gesamten Bewegungsapparats</li>
      </ul>
    </section>

    <section class="info-box info-box--composition">
      <h3>Zusammensetzung:</h3>
      <p>Brennessel, Kurkuma, Hagebutten,<br>Leinsamen, Löwenzahn</p>
      <p>Analytische Bestandteile:<br>Rohfaser 2,55%, Feuchtgehalt 12%</p>
    </section>

    <section class="info-box info-box--maker">
      <h3>Hersteller Information:</h3>
      <p>Petra Hollen<br>Lindenweg 14, 16247 Waldhagen DE</p>
    </section>

    <div class="brand-card">
      <span class="brand-card__dot"></span>
      <span class="brand-card__name">Anka's Pfotenwerk</span>
    </div>

    <h1 class="front front__title">NÄHRSTOFFPULVER</h1>
    <p class="front front__subtitle">für mehr Vitalität und Wohlbefinden<br>bei Hunden</p>
    <p class="front front__support">Unterstützung des</p>
    <div class="highlight"></div>
    <h2 class="highlight__word">Bewegungsapparats</h2>

    <svg class="dog-art" role="img" aria-label="Illustration eines springenden Hundes mit Blätterranke" viewBox="0 0 200 96">
      <rect x="0" y="0" width="200" height="96" rx="30" fill="#b8ad99"/>
    </svg>

    <div class="badge">
      <svg viewBox="0 0 86 86" width="86" height="86" aria-hidden="true">
        <circle cx="43" cy="43" r="41" fill="none" stroke="#efebe0" stroke-width="1"/>
      </svg>
      <p class="badge__text">100%<br>natürliche<br>Inhaltsstoffe</p>
    </div>

    <section class="info-box info-box--feeding">
      <h3>Fütterungsempfehlung:</h3>
      <p class="dose">• Hunde <b>bis 20kg - 1gr täglich</b><br>(reicht für 6 Monate)</p>
      <p class="dose">• Hunde <b>ab 20kg - 2gr täglich</b><br>(reicht für 3 Monate)</p>
      <p class="note">Das Pulver kann dem Futter<br>untergemischt werden.</p>
    </section>

    <p class="net-weight">Nettomasse: 200g</p>
    <p class="storage-hint">Hinweis: kühl, trocken und<br>lichtgeschützt lagern.</p>
    <div class="best-before">Mind.haltbar bis:</div>
  </main>
</body>
</html>
```